Design business card using existing logo.

PLEASE DO NOT USE "RED WHITE & BLACK" color combo! Thank you.

Try different color combos such as:
- Vintage colors like brown, orange, gold, blue (not all together but a combo of 1 or 3
- Blue, w/ grey, or silver or white, Blue monochromatic can work as well.
- Use monochromatic variations on back (just an idea)

- Include full name, "Quillmark Records" on at least one side.

Target Market(s)

Teens

Industry/Entity Type

Business

Colors
3277b5
ffc214
f04a50
f78f20

```html
<!DOCTYPE html>
<html lang="en">
<head>
<meta charset="utf-8">
<title>Quillmark Records — Business Card</title>
<link href="https://fonts.googleapis.com/css2?family=Lato:wght@400;700;900&display=swap" rel="stylesheet">
<style>
  :root {
    --brand-blue: #3277b5;
    --brand-yellow: #ffc214;
    --brand-red: #f04a50;
    --white: #ffffff;
    --stage: #e9e9ec;
    --blue-tint: rgba(255, 255, 255, 0.07);
    --yellow-tint: rgba(240, 160, 20, 0.22);
  }
  * { margin: 0; padding: 0; box-sizing: border-box; }
  html, body {
    width: 1200px;
    height: 780px;
    overflow: hidden;
    background: var(--stage);
    font-family: "Lato", sans-serif;
  }
  .canvas {
    position: relative;
    width: 1200px;
    height: 780px;
    display: flex;
    align-items: center;
    justify-content: center;
    gap: 40px;
  }
  .card {
    position: relative;
    width: 520px;
    height: 297px;
    overflow: hidden;
    box-shadow: 0 6px 18px rgba(0, 0, 0, 0.18);
  }
  .card--front { background: var(--brand-blue); color: var(--white); }
  .card--back { background: var(--brand-yellow); color: var(--white); }

  .deco-circle {
    position: absolute;
    border-radius: 50%;
  }
  .card--front .deco-circle {
    width: 300px; height: 300px;
    right: -40px; top: -70px;
    background: var(--blue-tint);
  }
  .card--back .deco-circle {
    width: 230px; height: 230px;
    right: -60px; top: -90px;
    background: var(--yellow-tint);
  }

  .brand {
    position: absolute;
    display: flex;
    flex-direction: column;
    align-items: center;
    gap: 12px;
  }
  .brand__dot {
    border-radius: 50%;
  }
  .brand__name {
    font-weight: 900;
    letter-spacing: 0.04em;
    text-transform: uppercase;
    line-height: 1;
    white-space: nowrap;
  }
  .card--front .brand { left: 24px; width: 220px; top: 98px; }
  .card--front .brand__dot { width: 52px; height: 52px; background: var(--brand-yellow); }
  .card--front .brand__name { font-size: 17px; color: var(--brand-yellow); }

  .card--back .brand { left: 0; right: 0; top: 72px; gap: 16px; }
  .card--back .brand__dot { width: 78px; height: 78px; background: var(--white); }
  .card--back .brand__name { font-size: 30px; color: var(--white); }

  .divider {
    position: absolute;
    left: 262px; top: 70px;
    width: 1px; height: 120px;
    background: rgba(255, 255, 255, 0.7);
  }
  .contact {
    position: absolute;
    left: 290px; top: 74px;
  }
  .contact__name {
    font-size: 20px;
    letter-spacing: 0.02em;
    text-transform: uppercase;
    line-height: 1.1;
  }
  .contact__name strong { font-weight: 900; }
  .contact__name span { font-weight: 400; }
  .contact__role {
    font-size: 11px;
    font-weight: 700;
    letter-spacing: 0.08em;
    color: var(--brand-yellow);
    text-transform: uppercase;
    margin-bottom: 12px;
  }
  .contact__list { list-style: none; }
  .contact__item {
    display: flex;
    align-items: center;
    gap: 9px;
    font-size: 12.5px;
    margin-bottom: 6px;
  }
  .contact__icon {
    width: 18px; height: 18px;
    border-radius: 50%;
    background: var(--brand-red);
    display: flex;
    align-items: center;
    justify-content: center;
    flex: none;
  }
  .address {
    position: absolute;
    left: 0; right: 0; bottom: 26px;
    text-align: center;
    font-size: 12.5px;
    letter-spacing: 0.02em;
  }
</style>
</head>
<body>
<main class="canvas">

  <section class="card card--front" aria-label="Business card front">
    <div class="deco-circle"></div>

    <div class="brand">
      <span class="brand__dot"></span>
      <span class="brand__name">Quillmark Records</span>
    </div>

    <div class="divider"></div>

    <div class="contact">
      <p class="contact__name"><strong>Marcus</strong> <span>Hale</span></p>
      <p class="contact__role">Managing Director</p>
      <ul class="contact__list">
        <li class="contact__item">
          <span class="contact__icon">
            <svg width="10" height="10" viewBox="0 0 24 24" fill="#fff"><path d="M6.6 10.8a15.1 15.1 0 0 0 6.6 6.6l2.2-2.2a1 1 0 0 1 1-.25 11.4 11.4 0 0 0 3.6.57 1 1 0 0 1 1 1V20a1 1 0 0 1-1 1A17 17 0 0 1 3 4a1 1 0 0 1 1-1h3.5a1 1 0 0 1 1 1c0 1.250.2 2.45.57 3.6a1 1 0 0 1-.25 1z"/></svg>
          </span>
          27 10 555 0148
        </li>
        <li class="contact__item">
          <span class="contact__icon">
            <svg width="10" height="10" viewBox="0 0 24 24" fill="none" stroke="#fff" stroke-width="2.4"><rect x="3" y="5" width="18" height="14" rx="1"/><path d="M3 6l9 7 9-7"/></svg>
          </span>
          marcus@quillmarkrec.com
        </li>
        <li class="contact__item">
          <span class="contact__icon">
            <svg width="10" height="10" viewBox="0 0 24 24" fill="none" stroke="#fff" stroke-width="2.2"><circle cx="12" cy="12" r="9"/><path d="M3 12h18M12 3c3 3.2 3 14.8 0 18M12 3c-3 3.2-3 14.8 0 18"/></svg>
          </span>
          www.quillmarkrec.com
        </li>
      </ul>
    </div>

    <p class="address">42 Harbor Lane South, Suite 210, Millbrook, NJ</p>
  </section>

  <section class="card card--back" aria-label="Business card back">
    <div class="deco-circle"></div>
    <div class="brand">
      <span class="brand__dot"></span>
      <span class="brand__name">Quillmark Records</span>
    </div>
  </section>

</main>
</body>
</html>
```